Trifold B2B flyer for software consulting/software futureproofness check / IT company

We need a flyer for a consulting offer for the company "VORANTEK GmbH".

The service involves the analysis and evaluation of software systems in companies; the target group consists of managing directors and IT managers of medium-sized companies in various industries.

The flyer should be modern, uncluttered, serious, and professional. It must inspire trust. A dark background would be preferable.

For content and layout, see PDF/PPTX "Software-Wandel-Fast-Scan-Konzept.pptx|.pdf".

In the appendix you will find further examples of VORANTEK designs, as well as the logo and other images.

-----------
We need a flyer for a consulting offering for the company “VORANTEK GmbH”.

The offering focuses on the analysis and evaluation of software systems within companies. The target audience is managing directors/CEOs and IT managers of mid-sized companies across various industries.

The flyer should be modern, clean, serious, and professional. It must build trust. A dark background is preferred.

Please refer to the PDF/PPTX “Software-Wandels-Fast-Scan-konzept.pptx|.pdf” for the content and the layout/ordering of the sections.

Attached you will also find additional examples of VORANTEK designs, as well as the logo and further images.

Target Market(s)

Medium businesses, various industries. Target group: CEO, CIO, IT lead

Industry/Entity Type

Medium-Businesses, various Industries.

Font styles to use
Sans Serif
Other font styles liked:
• Myriad

Colors

Designer to choose colors to be used in the design.

Requirements
Must have
• Branding of my company, professional, stylish, clean, trustful design

```html
<!DOCTYPE html>
<html lang="de">
<head>
<meta charset="utf-8">
<title>Software-Wandel-Fast-Scan – VORANTEK</title>
<link rel="stylesheet" href="https://fonts.googleapis.com/css2?family=Fira+Sans:wght@300;400;500;600;700&family=Kalam:wght@700&display=swap">
<style>
  :root {
    --bg-deep: #181c2b;
    --bg-mid: #232a3d;
    --bg-blue: #2a3352;
    --band: rgba(196, 198, 201, 0.88);
    --band-text: #34373c;
    --text: #f1f2f4;
    --accent: #3b7fd6;
    --rule: #f4f4f4;
  }
  * { margin: 0; padding: 0; box-sizing: border-box; }
  html, body { width: 1200px; height: 849px; overflow: hidden; background: var(--bg-deep); }
  body { font-family: "Fira Sans", sans-serif; color: var(--text); }

  .flyer { position: relative; width: 1200px; height: 849px; overflow: hidden; }
  .backdrop {
    position: absolute; inset: 0;
    background:
      radial-gradient(ellipse at 30% 35%, rgba(60, 72, 110, 0.55), transparent 60%),
      linear-gradient(160deg, var(--bg-mid) 0%, var(--bg-blue) 40%, var(--bg-deep) 100%);
  }

  .title {
    position: absolute; left: 20px; top: 17px;
    font-size: 28px; font-weight: 700; letter-spacing: -0.2px;
  }
  .subtitle {
    position: absolute; right: 21px; top: 27px;
    font-size: 18px; font-weight: 600;
  }

  .intro {
    position: absolute; left: 0; top: 66px; width: 1200px; height: 67px;
    background: var(--band); color: var(--band-text);
    padding: 9px 21px 0 20px;
    font-size: 18.5px; font-weight: 500; line-height: 23px;
  }
  .intro p:last-child { text-align: justify; text-align-last: justify; }

  .column { position: absolute; top: 164px; }
  .column--questions { left: 20px; width: 340px; }
  .column--process { left: 420px; width: 350px; }
  .column--results { left: 821px; width: 350px; }

  .column__heading {
    color: var(--accent); font-size: 24px; font-weight: 600;
    margin-bottom: 16px; line-height: 30px;
  }
  .column__list { list-style: none; padding-left: 13px; }
  .column__list li {
    position: relative; font-size: 19.5px; line-height: 24px; letter-spacing: 0.3px;
    margin-bottom: 16px; font-weight: 400;
    hyphens: auto; -webkit-hyphens: auto;
  }
  .column__list li::before,
  .facts__list li::before {
    content: ""; display: inline-block; margin-right: 6px; vertical-align: 2px;
    border-left: 6px solid var(--accent);
    border-top: 4px solid transparent; border-bottom: 4px solid transparent;
  }
  .column__list strong { font-weight: 600; letter-spacing: 0; }

  .chevron { position: absolute; width: 32px; height: 90px; }
  .chevron--first { left: 385px; top: 335px; }
  .chevron--second { left: 784px; top: 335px; }

  .divider {
    position: absolute; left: 20px; top: 608px; width: 1159px; height: 2px;
    background: var(--rule);
  }

  .brand { position: absolute; left: 20px; top: 646px; }
  .brand__mark {
    position: absolute; left: 0; top: 0; width: 22px; height: 26px;
    background: var(--accent);
  }
  .brand__name {
    position: absolute; left: 26px; top: 22px;
    font-size: 64px; font-weight: 600; letter-spacing: 6px; line-height: 70px;
    color: var(--text); white-space: nowrap;
  }
  .claim {
    position: absolute; left: 48px; top: 760px;
    font-family: "Kalam", cursive; font-weight: 700; font-size: 31px; line-height: 34px;
    color: var(--text); transform: rotate(-5deg); transform-origin: left top;
  }
  .claim span { display: block; padding-left: 78px; }

  .facts { position: absolute; }
  .facts--scope { left: 420px; top: 646px; width: 380px; }
  .facts__label { font-size: 17px; font-weight: 600; margin-bottom: 4px; }
  .facts__list { list-style: none; font-size: 15px; line-height: 24px; }
  .facts__list li::before { margin-right: 4px; border-left-width: 5px; border-top-width: 3.5px; border-bottom-width: 3.5px; }
  .facts__label--excluded { margin-top: 22px; margin-bottom: 2px; }
  .facts__list--excluded { line-height: 20px; }

  .facts--price { left: 821px; top: 644px; width: 360px; }
  .facts__heading { color: var(--accent); font-size: 24px; font-weight: 600; margin-bottom: 10px; }
  .facts__list--price { font-size: 19px; line-height: 33px; padding-left: 3px; }
  .facts__list--price strong { font-weight: 600; }
  .facts__upgrade {
    position: absolute; top: 151px; left: 0;
    font-size: 15px; line-height: 20px; font-weight: 400;
  }
  .facts__upgrade strong { font-weight: 600; }
</style>
</head>
<body>
<main class="flyer">
  <div class="backdrop" role="img" aria-label="Abgedunkelter Bildschirm mit Programmcode im Hintergrund"></div>

  <h1 class="title">Software-Wandel-Fast-Scan</h1>
  <p class="subtitle">Bestandssysteme: weiter investieren, modernisieren oder ersetzen?</p>

  <div class="intro">
    <p>Der Fast-Scan dient der schnellen Orientierung und Objektivierung.</p>
    <p>Er stellt die Basis für eine detaillierte Analyse des Bestandssystems in Punkto Zukunftsfähigkeit und Handlungsoptionen.</p>
  </div>

  <section class="column column--questions">
    <h2 class="column__heading">Fragestellungen</h2>
    <ul class="column__list">
      <li>Was sind die <strong>realen Risiken</strong> (Be&shy;trieb, Stabilität, Abhängigkeiten, Know-how)?</li>
      <li>Wo liegen die <strong>größten Kostentrei&shy;ber</strong> (Run-Kosten, Change-Kosten, Folgekosten)?</li>
      <li>Welche drei Wege sind grundsät&shy;zlich realistisch: <strong>Invest / Modernize / Replace?</strong></li>
      <li>Was müssen wir <strong>jetzt</strong> wissen, um innerhalb von 5–10 Tagen sauber entscheiden zu können?</li>
    </ul>
  </section>

  <svg class="chevron chevron--first" viewBox="0 0 32 90" aria-hidden="true"><polygon points="0,0 14,0 32,45 14,90 0,90 18,45" fill="#3b7fd6"/></svg>

  <section class="column column--process">
    <h2 class="column__heading">Vorgehen</h2>
    <ul class="column__list">
      <li><strong>Kickoff (60–90 Min)</strong>: Ziel, Kontext, Entscheidungsdruck, verfügbare Arte&shy;fakte</li>
      <li><strong>Sichtung &amp; Analyse:</strong> max. 10 Arte&shy;fakte (Kosten, Incidents, Roadmap, Architektur-Skizze, Vendor-Info)</li>
      <li><strong>2 Interviews (je 60–90 Min)</strong>: CIO / Owner + Head of Engineering/Tech Lead</li>
      <li><strong>Ergebnisgespräch (60 Min)</strong>: Ergeb&shy;nisse, Lücken, Empfehlung, nächster Schritt</li>
    </ul>
  </section>

  <svg class="chevron chevron--second" viewBox="0 0 32 90" aria-hidden="true"><polygon points="0,0 14,0 32,45 14,90 0,90 18,45" fill="#3b7fd6"/></svg>

  <section class="column column--results">
    <h2 class="column__heading">Ergebnisse / Lieferobjekte</h2>
    <ul class="column__list">
      <li><strong>Decision Snapshot</strong>: Status, Top-Risiken, wesentliche TCO-Trei&shy;ber, offene Entscheidungsfragen (One-Pager)</li>
      <li><strong>3-Optionen-Skizze</strong>: Modernize / Replace / Invest mit Pros/Cons und Abhängigkeiten (One-Pager)</li>
      <li><strong>Gap-Liste</strong>: Welche Informationen fehlen für eine saubere Entscheidung (Max. 10 Punkte)</li>
      <li><strong>Go/No-Go-Empfehlung</strong>: Mögliche nächste Schritte und Handlungsop&shy;tionen</li>
    </ul>
  </section>

  <div class="divider"></div>

  <div class="brand">
    <span class="brand__mark"></span>
    <span class="brand__name">VORANTEK</span>
  </div>
  <p class="claim">Klarer Kurs<span>in kurzer Zeit</span></p>

  <section class="facts facts--scope">
    <h3 class="facts__label">Scope:</h3>
    <ul class="facts__list">
      <li>1 System</li>
      <li>1–2 Calls + Doku-Sichtung</li>
      <li>Ergebnis als kompakte Entscheidungsunterlagen</li>
    </ul>
    <h3 class="facts__label facts__label--excluded">Nicht enthalten:</h3>
    <ul class="facts__list facts__list--excluded">
      <li>Detail-Spezifikation, Ausschreibung, Umsetzung, Tool-Auswahlprozess im Vollumfang</li>
    </ul>
  </section>

  <section class="facts facts--price">
    <h2 class="facts__heading">Preis &amp; Dauer:</h2>
    <ul class="facts__list facts__list--price">
      <li><strong>Preis: 3.500–5.000 €</strong> (zzgl. USt)</li>
      <li><strong>Dauer: 1 Woche</strong></li>
    </ul>
    <p class="facts__upgrade">Upgrade möglich zum umfassenden <strong>Software-Wandel-Check</strong></p>
  </section>
</main>
</body>
</html>
```